Brantley Fuel Retro Website Design

Have a logo. Need a website design to go along with the logo design. Full Design Specs are here: https://files.quormbex.net/doc/8QwLp2ZtR4vNx7sYh3JkM9aDc5Ub6FgTe1WiO0rVn2X/view

Target Market(s)

Independent Gas Station Owners

Number of Pages Required

1 page

Font styles to use
Sans Serif

Colors

Designer to choose colors to be used in the design.

```html
<!DOCTYPE html>
<html lang="en">
<head>
<meta charset="utf-8">
<title>Brantley Fuel</title>
<link href="https://fonts.googleapis.com/css2?family=Pacifico&family=Playfair+Display:wght@400;700&family=Roboto:wght@400;500;700&display=swap" rel="stylesheet">
<style>
:root{
  --red:#e5363d;
  --red-dark:#c92a31;
  --ink:#1c1e1f;
  --ink-2:#272a2b;
  --cream:#f8f4e8;
  --paper:#ffffff;
  --grey:#8a8a8a;
  --text:#3a3a3a;
  --orange:#f3a21c;
  --script:'Pacifico',cursive;
  --serif:'Playfair Display',serif;
  --sans:'Roboto',sans-serif;
}
*{box-sizing:border-box;margin:0;padding:0}
html,body{width:1200px;height:2880px;overflow:hidden}
body{position:relative;background:var(--cream);font-family:var(--sans);color:var(--text)}
.abs{position:absolute}
.script{font-family:var(--script);font-weight:400}

/* hero */
.hero-dark{left:0;top:0;width:1200px;height:670px;background:var(--ink)}
.hero-shape{left:0;top:0}
.topline{left:692px;top:13px;font-size:10px;color:#fff;display:flex;gap:8px;align-items:center}
.topline .phone{color:var(--red);font-family:var(--serif);font-size:15px}
.topline em{font-family:var(--serif);font-size:9px;color:#aaa}
.nav{left:300px;top:44px;width:600px;height:37px;background:var(--paper);border-radius:19px;box-shadow:0 3px 10px rgba(0,0,0,.25);font-size:9px;text-transform:uppercase;color:#333}
.nav span{position:absolute;top:14px}
.nav .on{color:var(--red)}
.nav .dot{color:var(--orange)}
.brand{left:552px;top:22px;width:96px;height:80px;text-align:center}
.brand .mark{width:54px;height:54px;border-radius:50%;background:var(--red);margin:0 auto;border:4px solid var(--ink)}
.brand .name{font-family:var(--serif);font-weight:700;font-size:12px;color:var(--ink);background:var(--paper);margin-top:-6px;padding:2px 0;border-radius:4px}
.truck{left:0;top:115px;width:305px;height:225px;border-radius:30px;background:linear-gradient(135deg,#f6c36b,#c2392f)}
.pump{left:330px;top:120px;width:80px;height:225px;border-radius:20px;background:linear-gradient(#f0b25a,#d9534f)}
.hero-title{left:340px;top:132px;width:260px;font-size:27px;line-height:36px;color:#fff;text-align:right}
.hero-copy{left:405px;top:226px;width:182px;font-family:var(--serif);font-size:7.5px;line-height:10px;color:var(--ink);text-align:right}
.hire{left:693px;top:138px;font-size:19px;color:var(--red)}
.lbl{font-size:8px;color:#999;font-family:var(--serif)}
.field{background:#161818;height:28px;width:207px}
.pinbtn{left:688px;top:266px;width:74px;height:20px;background:#2c2f30;color:#fff;font-size:7px;display:flex;align-items:center;gap:4px;padding-left:6px}
.addr{left:770px;top:272px;font-size:7px;color:#aaa}
.btn{background:var(--red);color:#fff;font-family:var(--serif);font-weight:700;font-size:11px;display:flex;align-items:center;justify-content:center;gap:9px;border:1px solid #fff3}
.tick{width:17px;height:17px;border-radius:50%;border:1.5px solid #fff;display:flex;align-items:center;justify-content:center}

/* services */
.card{left:166px;top:548px;width:886px;height:520px;background:var(--cream)}
.h2{font-size:31px;color:var(--ink);text-align:center;width:1200px;left:0}
.rule{height:0;border-top:1px dotted #c9c2ae;width:230px}
.lead{left:437px;top:676px;width:326px;text-align:center;font-family:var(--serif);font-size:10.5px;line-height:12px;color:#555}
.grid{left:180px;top:812px;width:855px;height:428px;display:grid;grid-template-columns:repeat(4,1fr);grid-template-rows:repeat(2,1fr)}
.cell{position:relative}
.cell.red{background:var(--red);color:#fff;text-align:center;padding:30px 16px 0}
.cell.red h3{font-family:var(--script);font-weight:400;font-size:20px}
.cell.red hr{width:28px;border:0;border-top:2px solid #fff;margin:4px auto 16px}
.cell.red p{font-size:8.3px;line-height:15px;font-weight:500}
.notch-l::before,.notch-r::after{content:"";position:absolute;top:50%;margin-top:-11px;border:11px solid transparent}
.notch-l::before{left:-22px;border-right-color:var(--red)}
.notch-r::after{right:-22px;border-left-color:var(--red)}
.ph{width:100%;height:100%}

/* how */
.sub{left:0;width:1200px;text-align:center;font-family:var(--serif);font-size:8.5px;color:#555}
.step{width:200px;height:70px}
.step .circ{position:absolute;left:0;top:0;width:64px;height:64px;border-radius:50%;background:#fff;box-shadow:0 2px 8px rgba(0,0,0,.08);display:flex;align-items:center;justify-content:center}
.step h4{position:absolute;left:78px;top:8px;font-family:var(--serif);font-weight:400;font-size:13px;color:#333}
.step p{position:absolute;left:78px;top:28px;width:95px;font-family:var(--serif);font-size:8px;line-height:9.5px;color:#888}

/* questions */
.q{left:0;top:1515px;width:1200px;height:350px;background:linear-gradient(180deg,#2a2c2d,#1b1d1e)}
.envelope{left:283px;top:1560px;width:330px;height:270px;background:linear-gradient(135deg,#efeadc,#d9d3c1);transform:rotate(-4deg)}
.form{left:300px;top:1545px;width:237px;height:292px;background:#fff;box-shadow:0 4px 14px rgba(0,0,0,.4)}
.form .lbl{position:absolute;left:29px}
.form .in{position:absolute;left:29px;width:179px;height:27px;background:#ececec}
.qh{left:656px;top:1622px;font-size:30px;line-height:40px;color:#fff}
.qh span{color:var(--red)}
.qp{left:656px;top:1719px;width:242px;font-family:var(--serif);font-size:7.5px;line-height:9.5px;color:#fff}

/* gallery */
.gal-bg{left:0;top:1865px;width:1200px;height:465px;background:#fff}
.g{position:absolute}

/* news */
.news-dark{left:0;top:2630px;width:1200px;height:213px;background:var(--ink)}
.news{left:300px;top:2376px;width:300px;height:329px;background:#fff}
.news .head{height:62px;background:var(--red);position:relative}
.head .t{position:absolute;left:22px;top:10px;font-size:25px;color:#fff}
.head .more{position:absolute;right:22px;top:28px;font-family:var(--serif);font-size:7.5px;color:#fff;text-decoration:underline}
.item{position:absolute;left:0;width:300px}
.item .d{position:absolute;left:15px;top:0;font-family:var(--serif);font-size:21px;color:var(--red)}
.item .m{position:absolute;left:15px;top:30px;font-size:6px;color:#aaa}
.item .b{position:absolute;left:55px;top:8px;width:5px;height:5px;border-radius:50%;background:var(--orange)}
.item h5{position:absolute;left:79px;top:0;width:200px;font-family:var(--serif);font-weight:400;font-size:11px;line-height:13px;color:#444}
.item p{position:absolute;left:79px;top:32px;width:200px;font-size:7px;line-height:8.5px;color:#aaa}
.specials{left:600px;top:2376px;width:300px;height:329px}
.specials .head{background:var(--ink)}
.sp1{position:absolute;left:0;top:62px;width:300px;height:133px;background:#ecebe4}
.sp2{position:absolute;left:0;top:195px;width:300px;height:134px;background:linear-gradient(90deg,#f29a12,#f7b32d)}

/* footer */
.foot-l{left:300px;top:2754px;width:190px;font-size:6.5px;line-height:8px;color:#999}
.copy{left:300px;top:2793px;font-size:6.5px;color:#999}
.foot-c{left:557px;top:2733px;width:86px;height:86px;border-radius:50%;background:#161818;text-align:center;padding-top:28px}
.foot-c b{font-family:var(--serif);font-weight:400;color:var(--red);font-size:14px;display:block}
.foot-c em{font-family:var(--serif);font-size:7px;color:#aaa}
.foot-r{left:700px;top:2752px;width:200px;text-align:right;font-size:7px;color:#999;line-height:10px}
.foot-r b{color:#fff;font-weight:500;font-size:8px}
.soc{top:2781px;width:22px;height:22px;border-radius:50%;background:var(--red);border:2px solid #fff}
.bar{left:0;top:2843px;width:1200px;height:37px;background:var(--red);font-size:7px;color:#fff;display:flex;justify-content:center;align-items:center;gap:10px}
</style>
</head>
<body>

<!-- hero -->
<div class="abs hero-dark"></div>
<svg class="abs hero-shape" width="1200" height="670" viewBox="0 0 1200 670">
  <polygon points="0,0 600,0 600,418 0,448" fill="#e5363d"/>
  <polygon points="166,548 1052,548 1052,622 1200,616 1200,670 0,670 0,666 166,666" fill="#f8f4e8"/>
</svg>

<div class="abs topline"><span>USA</span><span class="dot" style="color:#e5363d">•</span><span class="phone">#615</span><em>Call us any time</em></div>

<nav class="abs nav">
  <span style="left:39px">Home</span><span class="dot" style="left:77px">•</span>
  <span class="on" style="left:93px">Services</span><span class="dot" style="left:147px">•</span>
  <span style="left:163px">Booking</span>
  <span style="left:393px">Blog</span><span class="dot" style="left:429px">•</span>
  <span style="left:445px">About</span><span class="dot" style="left:487px">•</span>
  <span style="left:503px">Contact</span>
  <svg style="position:absolute;left:573px;top:13px" width="11" height="11" viewBox="0 0 11 11"><circle cx="4.5" cy="4.5" r="3.5" fill="none" stroke="#aaa" stroke-width="1.2"/><line x1="7" y1="7" x2="10" y2="10" stroke="#aaa" stroke-width="1.2"/></svg>
</nav>
<div class="abs brand"><div class="mark"></div><div class="name">Brantley Fuel</div></div>

<div class="abs truck" role="img" aria-label="Retro illustration of a delivery truck"></div>
<div class="abs pump" role="img" aria-label="Retro illustration of a gas pump"></div>
<h1 class="abs hero-title script">There are many variations passages</h1>
<p class="abs hero-copy">There are many variations of passages of Lorem Ipsum available, but the majority</p>

<div class="abs hire script">Hire Us</div>
<div class="abs lbl" style="left:655px;top:190px">Name:</div>
<div class="abs field" style="left:688px;top:182px"></div>
<div class="abs lbl" style="left:654px;top:224px">Phone:</div>
<div class="abs field" style="left:688px;top:216px"></div>
<div class="abs lbl" style="left:652px;top:271px">Adress:</div>
<div class="abs pinbtn"><svg width="7" height="9" viewBox="0 0 7 9"><path d="M3.5 0A3.2 3.2 0 0 0 .3 3.2C.3 5.6 3.5 9 3.5 9s3.2-3.4 3.2-5.8A3.2 3.2 0 0 0 3.5 0z" fill="#e5363d"/></svg>Chose on map</div>
<div class="abs addr">Dalton, 2290 Marlow Rd</div>
<div class="abs btn" style="left:688px;top:316px;width:79px;height:28px">Done <span class="tick"><svg width="8" height="7" viewBox="0 0 8 7"><path d="M1 3.5l2 2L7 1" stroke="#fff" stroke-width="1.4" fill="none"/></svg></span></div>

<!-- services -->
<h2 class="abs h2 script" style="top:584px">Our Services</h2>
<div class="abs rule" style="left:227px;top:612px"></div>
<div class="abs rule" style="left:758px;top:612px"></div>
<p class="abs lead">There are many variations of passages of Lorem Ipsum available, but the majority have suffered alteration in some form, by injected humour, or randomised words which don't look even slightly believable. If you are going to use a passage of Lorem Ipsum, you need to be sure there isn't anything</p>

<div class="abs grid">
  <div class="cell"><div class="ph" role="img" aria-label="Photo of a white fuel delivery tank truck" style="background:linear-gradient(135deg,#6f7472,#d9dcd8 55%,#585d5c)"></div></div>
  <div class="cell red notch-l"><h3>Fuel Delivery</h3><hr><p>Brantley Fuel provides fuel delivery for independent gas stations, convenience stores, construction sites or any other commercial need. If you are looking for gasoline, high sulfer diesel fuel, farm diesel or other bulk fuel delivered to your business, we will take care of you!</p></div>
  <div class="cell"><div class="ph" role="img" aria-label="Photo of motor oil bottles" style="background:radial-gradient(circle,#9aa1a6,#f4f4f4 70%)"></div></div>
  <div class="cell red notch-l"><h3>Oil</h3><hr><p>Looking for speciality auto, tractor, tractor trailer, aviation or other commercial oils and lubricants Brantley Fuel can help! Just call one of our customer oriented staff and we will get what you need quick! We have a complete line of aviation oils and lubricants as well as gear lubricants, greases, oils and more!</p></div>
  <div class="cell red notch-r"><h3>Farm Fuel</h3><hr><p>Looking for gasoline, diesel red diesel off road fuel or farm diesel? We can deliver straight to your farm! We can setup your farm tanks, take care of EPA containment and deliver fuel when you need it!</p></div>
  <div class="cell"><div class="ph" role="img" aria-label="Photo of white farm fuel tanks" style="background:linear-gradient(180deg,#7b7a72,#e6e6e2 55%,#8c8677)"></div></div>
  <div class="cell red notch-r"><h3>Cargo Containers</h3><hr><p>Want to purchase or lease a storage container, we have what you need! We can deliver or move storage containers to your home, business, construction site or any you need one! .</p></div>
  <div class="cell"><div class="ph" role="img" aria-label="Photo of a grey cargo container" style="background:linear-gradient(180deg,#8c8f8c,#b7bcbd 50%,#8a8579)"></div></div>
</div>

<!-- how it works -->
<h2 class="abs h2 script" style="top:1292px">How it works</h2>
<p class="abs sub" style="top:1339px">There are many variations of passages of Lorem Ipsum available</p>

<div class="abs step" style="left:298px;top:1401px">
  <div class="circ"><svg width="16" height="22" viewBox="0 0 16 22"><rect x="2" y="1" width="12" height="20" rx="2" fill="none" stroke="#e5363d" stroke-width="1.4"/><line x1="6" y1="18" x2="10" y2="18" stroke="#e5363d" stroke-width="1.4"/></svg></div>
  <h4>Call Us</h4><p>There are many variations of passagesof Lorem Ipsum available but</p>
</div>
<div class="abs step" style="left:511px;top:1401px">
  <div class="circ"><svg width="22" height="22" viewBox="0 0 22 22" fill="none" stroke="#e5363d" stroke-width="1.3"><circle cx="11" cy="11" r="9"/><ellipse cx="11" cy="11" rx="4" ry="9"/><line x1="2" y1="11" x2="20" y2="11"/></svg></div>
  <h4>Choose Service</h4><p>There are many variations of passagesof Lorem Ipsum available but</p>
</div>
<div class="abs step" style="left:724px;top:1401px">
  <div class="circ"><svg width="24" height="18" viewBox="0 0 24 18" fill="none" stroke="#e5363d" stroke-width="1.3"><rect x="1" y="2" width="14" height="10"/><path d="M15 5h4l4 4v3h-8z"/><circle cx="6" cy="14" r="2.2"/><circle cx="18" cy="14" r="2.2"/></svg></div>
  <h4>We Deliver</h4><p>There are many variations of passagesof Lorem Ipsum available but</p>
</div>

<!-- questions -->
<section class="abs q" role="img" aria-label="Dark photo of the fuel depot building and parked trucks"></section>
<div class="abs envelope" role="img" aria-label="Illustration of stacked envelopes"></div>
<div class="abs form">
  <div class="lbl" style="top:36px">Name:</div><div class="in" style="top:51px"></div>
  <div class="lbl" style="top:88px">Email:</div><div class="in" style="top:103px"></div>
  <div class="lbl" style="top:140px">Message:</div><div class="in" style="top:155px;height:57px"></div>
  <div class="btn" style="position:absolute;left:29px;top:232px;width:79px;height:28px">Send <span class="tick"><svg width="8" height="7" viewBox="0 0 8 7"><path d="M1 3.5l2 2L7 1" stroke="#fff" stroke-width="1.4" fill="none"/></svg></span></div>
</div>
<h2 class="abs qh script">Have any<br><span>Questions?</span></h2>
<p class="abs qp">There are many variations of passages of Lorem Ipsum available, but the majority have suffered alteration in some form, by injected humour, or randomised words which don't look even slightly believable. If you are going to use a passage of Lorem Ipsum, you need to be sure there isn't anything</p>

<!-- gallery -->
<div class="abs gal-bg"></div>
<h2 class="abs h2 script" style="top:1886px">Our Gallery</h2>
<div class="abs rule" style="left:300px;top:1913px;width:215px;border-top-style:solid;border-color:#e5e5e5"></div>
<div class="abs rule" style="left:688px;top:1913px;width:212px;border-top-style:solid;border-color:#e5e5e5"></div>
<p class="abs sub" style="top:1948px">There are many variations of passages of Lorem Ipsum available</p>
<div class="g" style="left:300px;top:1985px;width:150px;height:144px;background:linear-gradient(180deg,#9a9a9a,#dcdcdc 55%,#777)" role="img" aria-label="Black and white photo of the company office"></div>
<div class="g" style="left:300px;top:2133px;width:150px;height:144px;background:linear-gradient(180deg,#555,#8a8a8a 50%,#3e3e3e)" role="img" aria-label="Black and white photo of workshop machinery"></div>
<div class="g" style="left:454px;top:1985px;width:293px;height:292px;background:linear-gradient(180deg,#9da2a6,#e9eaea 45%,#6e6a62)" role="img" aria-label="Photo of white semi trucks parked in a yard"></div>
<div class="g" style="left:454px;top:2121px;width:15px;height:20px;background:var(--ink)"></div>
<div class="g" style="left:732px;top:2121px;width:15px;height:20px;background:var(--red)"></div>
<svg class="g" style="left:458px;top:2127px" width="8" height="8" viewBox="0 0 8 8"><path d="M6 0L1 4l5 4z" fill="#fff"/></svg>
<svg class="g" style="left:736px;top:2127px" width="8" height="8" viewBox="0 0 8 8"><path d="M2 0l5 4-5 4z" fill="#fff"/></svg>
<div class="g" style="left:750px;top:1985px;width:150px;height:144px;background:linear-gradient(135deg,#a7acaf,#c9cdcf 55%,#8c8f90)" role="img" aria-label="Photo of a grey cargo container"></div>
<div class="g" style="left:750px;top:2133px;width:150px;height:144px;background:linear-gradient(180deg,#8e8c84,#e7e7e4 55%,#99948a)" role="img" aria-label="Photo of white fuel tanks"></div>

<!-- news & specials -->
<div class="abs news-dark"></div>
<div class="abs news">
  <div class="head"><span class="t script">News</span><span class="more">More news ›</span></div>
  <div class="item" style="top:93px"><span class="d">25</span><span class="m">Sep 2016</span><span class="b"></span><h5>There are many variations of passag-es of Lorem Ipsum available</h5><p>The generated Lorem Ipsum is therefore always free from repetition, injected humour, or non-characteristic...</p></div>
  <div class="item" style="top:176px"><span class="d">17</span><span class="m">Sep 2016</span><span class="b"></span><h5>There are many variations of passag-es of Lorem Ipsum available</h5><p>The generated Lorem Ipsum is therefore always free from repetition, injected humour, or non-characteristic...</p></div>
  <div class="item" style="top:258px"><span class="d">13</span><span class="m">Sep 2016</span><span class="b"></span><h5>There are many variations of passag-es of Lorem Ipsum available</h5><p>The generated Lorem Ipsum is therefore always free from repetition, injected humour, or non-characteristic...</p></div>
</div>
<div class="abs specials">
  <div class="head" style="height:62px;position:relative"><span class="t script" style="position:absolute;left:22px;top:10px;font-size:25px;color:#fff">Specials</span><span class="more" style="position:absolute;right:22px;top:28px;font-family:var(--serif);font-size:7.5px;color:#fff;text-decoration:underline">More specials ›</span></div>
  <div class="sp1">
    <div style="position:absolute;left:8px;top:8px;width:120px;height:120px;background:linear-gradient(135deg,#c9b79b,#ecebe4)" role="img" aria-label="Illustration of an oil pump jack"></div>
    <div style="position:absolute;left:171px;top:50px;font-size:10px;line-height:13px;color:#444">All the Lorem Ipsum<br>generators on the web</div>
    <div style="position:absolute;left:171px;top:80px;font-size:6px;color:#aaa">Lorem Ipsum passages</div>
  </div>
  <div class="sp2" role="img" aria-label="Illustration of taxis with a large fifty percent off offer">
    <div style="position:absolute;left:27px;top:70px;font-size:13px;line-height:12px;color:#fff;text-align:center">Specials<br>offer</div>
    <div class="script" style="position:absolute;left:100px;top:12px;font-size:72px;line-height:100px;color:#fff">-50%</div>
  </div>
</div>

<!-- footer -->
<p class="abs foot-l">There are many variations of passages of Lorem Ipsum available generated Lorem Ipsum is therefore always free from repetition, injected humour, or non-characteristic...</p>
<p class="abs copy">© 2019 Brantley Fuel. All rights reserved</p>
<div class="abs foot-c"><b>#615</b><em>Call us any time</em></div>
<div class="abs foot-r">Our adress:<br><b>UK, Leeds, 2290 Marlow Rd</b></div>
<div class="abs soc" style="left:817px"></div>
<div class="abs soc" style="left:846px"></div>
<div class="abs soc" style="left:875px"></div>
<div class="abs bar"><span>Our blog</span><span style="color:var(--orange)">•</span><span>Contat form</span><span style="color:var(--orange)">•</span><span>Sitemap</span></div>

</body>
</html>
```